Redesigning of the packaging for 4 MORNING VELVET gourmet breads

We need new designs for our range of four gourmet sliced breads, called MORNING VELVET. These breads are prepared with specially selected ingredients sourced from several countries and with extreme focus on quality, health and indulgent pleasure. The Morning Velvet brand aims to solve the boring and bland nature of white breads and comes in several flavours such as coconut, seeds & nuts, exotic fruits and vegetables, buttermilk, chocolate, etc.
The Morning Velvet brand positioning statement is JOY IN EVERY SLICE
The current packaging designs are still quite attractive which makes it a difficult decision, but we know it's time for a rebrand, and therefore we really want the best possible designs - ONLY THE BEST!
MORNING VELVET currently comprises three 'sister' products and one new addition named as follows:
1. Morning Velvet - buttermilk bliss (yellow color)
2. Morning Velvet - choco delight (brown & orange color)
3. Morning Velvet - creamy coconut (green & cream color)
4. Morning Totz - (kiddies' style - This is a kiddies bread)
[Some pictures of the current packaging are attached, alongside with the content, layout and dimensions which should be used for the new designs, including ingredients, addresses, etc. Check the file 'Back view with ingredients and contents.pdf'; 'Layout and Dimensions of current Morning Velvet Packaging.pdf]
5. The logo may or may not be modified. (Morning Velvet Logo.pdf)
Key points to note:
- Demographic: The target audience is mainly young and middle aged from the middle to upper economic class
- Psychographic: Health conscious, Class conscious, Family focused consumers, Environment and Sustainable development minded consumers
- The designs will be similar in style for the 3 variants but be differentiated by colours and content
- The fonts and the overall design should be modern, playful and inviting.
- The content of the packaging is in the attachments
- Total designs - 4 designs.
Target Market(s)
The target market is kids, teens, young adults. Middle to upper economic class. Premium segment, lifestyle conscious consumers.
Industry/Entity Type
Bakery
Colors
Designer to choose colors to be used in the design.
Look and feel
Each slider illustrates characteristics of the customer's brand and the style your logo design should communicate.

```html
<!DOCTYPE html>
<html lang="en">
<head>
<meta charset="utf-8">
<title>Morning Velvet – Buttermilk Bread Pack</title>
<link href="https://fonts.googleapis.com/css2?family=Lilita+One&display=swap" rel="stylesheet">
<style>
  :root {
    --bg: #ffffff;
    --bag-yellow: #f0cf1e;
    --bag-light: #fff4a8;
    --bag-shade: #d6b10e;
    --title-blue: #1f4fc6;
    --title-navy: #0e2466;
    --pill-orange: #f29a12;
    --pill-deep: #c8650a;
    --window-red: #d8262b;
    --bread-light: #d6b88c;
    --bread-dark: #6e4a2c;
    --brand-green: #1e7a2e;
    --white: #ffffff;
  }
  html, body {
    margin: 0;
    padding: 0;
    width: 1200px;
    height: 464px;
    overflow: hidden;
    background: var(--bg);
  }
  .pack-canvas {
    display: block;
    width: 1200px;
    height: 464px;
  }
  .product-title,
  .product-title-shadow {
    font-family: "Lilita One", sans-serif;
    font-size: 64px;
    stroke-linejoin: round;
  }
  .product-title {
    fill: var(--title-blue);
    stroke: var(--white);
    stroke-width: 6px;
    paint-order: stroke fill;
  }
  .product-title-shadow {
    fill: var(--title-navy);
    stroke: var(--title-navy);
    stroke-width: 6px;
  }
  .flavour-label {
    font-family: "Lilita One", sans-serif;
    font-size: 20px;
    fill: var(--white);
    letter-spacing: 0.5px;
  }
  .maker-name {
    font-family: "Lilita One", sans-serif;
    font-size: 17px;
    fill: var(--brand-green);
  }
</style>
</head>
<body>
<svg class="pack-canvas" viewBox="0 0 1200 464" xmlns="http://www.w3.org/2000/svg">
  <defs>
    <radialGradient id="bag-glow" cx="300" cy="220" r="620" gradientUnits="userSpaceOnUse">
      <stop offset="0" stop-color="var(--bag-light)"/>
      <stop offset="0.4" stop-color="var(--bag-yellow)"/>
      <stop offset="1" stop-color="var(--bag-shade)"/>
    </radialGradient>
    <linearGradient id="bag-sheen" x1="0" y1="0" x2="0" y2="1">
      <stop offset="0" stop-color="#ffffff" stop-opacity="0.3"/>
      <stop offset="0.2" stop-color="#ffffff" stop-opacity="0"/>
      <stop offset="0.85" stop-color="#000000" stop-opacity="0"/>
      <stop offset="1" stop-color="#000000" stop-opacity="0.12"/>
    </linearGradient>
    <linearGradient id="bread-tone" x1="0" y1="0" x2="1" y2="1">
      <stop offset="0" stop-color="var(--bread-light)"/>
      <stop offset="0.55" stop-color="#9c7650"/>
      <stop offset="1" stop-color="var(--bread-dark)"/>
    </linearGradient>
    <linearGradient id="pill-fill" x1="0" y1="0" x2="0" y2="1">
      <stop offset="0" stop-color="var(--pill-orange)"/>
      <stop offset="1" stop-color="var(--pill-deep)"/>
    </linearGradient>
  </defs>

  <g class="bread-bag">
    <path class="bag-shape" fill="url(#bag-glow)"
      d="M112 92 C400 84 650 84 830 92 C872 96 880 150 905 200 C925 230 935 232 952 214 C990 170 1020 130 1045 115 L1062 108 L1072 120 L1085 104 L1098 112 L1092 150 L1106 182 L1096 222 L1110 262 L1098 300 L1104 340 L1088 362 L1070 354 L1050 364 C1020 345 985 300 955 272 C935 256 925 258 905 285 C880 330 870 376 830 380 C650 386 400 388 112 382 C92 382 84 372 84 352 L84 122 C84 102 92 92 112 92 Z"/>
    <path class="bag-sheen" fill="url(#bag-sheen)"
      d="M112 92 C400 84 650 84 830 92 C872 96 880 150 905 200 C925 230 935 232 952 214 C990 170 1020 130 1045 115 L1062 108 L1072 120 L1085 104 L1098 112 L1092 150 L1106 182 L1096 222 L1110 262 L1098 300 L1104 340 L1088 362 L1070 354 L1050 364 C1020 345 985 300 955 272 C935 256 925 258 905 285 C880 330 870 376 830 380 C650 386 400 388 112 382 C92 382 84 372 84 352 L84 122 C84 102 92 92 112 92 Z"/>
  </g>

  <g class="product-window">
    <path class="window-bread" role="img" aria-label="Sliced buttermilk loaf seen through the window"
      fill="url(#bread-tone)"
      d="M482 384 L480 240 C480 195 505 170 545 170 C575 170 592 190 602 212 C620 178 645 160 685 162 C745 166 800 215 802 275 C804 325 775 360 742 384 Z"/>
    <path class="window-frame" fill="none" stroke="var(--window-red)" stroke-width="6"
      d="M482 384 L480 240 C480 195 505 170 545 170 C575 170 592 190 602 212 C620 178 645 160 685 162 C745 166 800 215 802 275 C804 325 775 360 742 384"/>
  </g>

  <g class="maker-mark">
    <circle cx="420" cy="146" r="7" fill="var(--brand-green)"/>
    <text class="maker-name" x="432" y="152">Golden Crumb</text>
  </g>

  <g class="title-block" transform="rotate(-4 300 250)">
    <g transform="skewX(-8) translate(30 0)">
      <text class="product-title-shadow" x="142" y="226">MORNING</text>
      <text class="product-title" x="138" y="222">MORNING</text>
      <text class="product-title-shadow" x="214" y="284">VELVET</text>
      <text class="product-title" x="210" y="280">VELVET</text>
    </g>
  </g>

  <g class="flavour-pill">
    <rect x="252" y="294" width="150" height="32" rx="16" fill="url(#pill-fill)" stroke="var(--white)" stroke-width="3"/>
    <text class="flavour-label" x="327" y="317" text-anchor="middle">BUTTER MILK</text>
  </g>
</svg>
</body>
</html>
```